Brand and Marketing Coach Needs PDF Designed

I have content that i need placed into a simple but great PDF design. The PDF is about the formula I use to build personal brands. This is geared towards entrepreneurs, experts, coaches, therapists, wellness practitioners, and indpendent business owners who serve to improve the lives of others.
The company name is changing from Corvelta Studio to Growth with Neighbors (I don't have that logo yet, so working backwards a bit. For now, the Corvelta Studio logo can be used.) My brand is NOT formal and corporate, but it's also not neon-pink and screaming at you. It's down to earth, hip, a bit modern but warm. It's about no BS and authenticity. The final deliverable should make the reader feel focused, smart, motivated and hopeful.

Target Market(s)

Conscious entrepreneurs and small business owners. this one is specifically for pharmacy entrepreneurs but this will be used for various audiences later.

Font styles to use
Sans Serif

Colors
eaf1f7
3377b5
6b449b
f37122
faa54b
f68e4e
ffc214

Requirements
Must have
• Modern design. colors that match logo - 4e5583 (i think that is the blue.) d65a40.
• Could have these colors as well: c6a254, 01bcc3
• But open to other colors
Nice to have
• I'd like to see some ways to make this PDF simple and readable, and eye-catching. I'd also like to use the uploaded ebooks for design ideas.
Should not have
• neon colors, clip art

```html
<!DOCTYPE html>
<html lang="en">
<head>
<meta charset="utf-8">
<title>The Personal Brand Formula – Page Spreads</title>
<link href="https://fonts.googleapis.com/css2?family=EB+Garamond:ital,wght@0,400;0,500;0,600;1,400&family=Playfair+Display+SC&family=Allura&display=swap" rel="stylesheet">
<style>
  :root {
    --indigo: #4e5583;
    --ink: #1c1c1c;
    --paper: #ffffff;
    --frame: #8a8a8a;
    --photo-light: #d9d9d9;
    --photo-dark: #4a4a4a;
  }
  * { margin: 0; padding: 0; box-sizing: border-box; }
  html, body { width: 794px; height: 1200px; overflow: hidden; background: var(--paper); }
  body { position: relative; font-family: "EB Garamond", Georgia, serif; color: var(--ink); }

  .page {
    position: absolute; width: 356px; height: 276px;
    background: var(--paper); border: 1px solid var(--frame); overflow: hidden;
  }
  .col-left { left: 33px; }
  .col-right { left: 402px; }
  .row-1 { top: 26px; }
  .row-2 { top: 315px; }
  .row-3 { top: 607px; }
  .row-4 { top: 895px; }

  /* Cover */
  .cover-photo {
    position: absolute; left: 0; top: 0; width: 100%; height: 105px;
    background: linear-gradient(100deg, var(--photo-light) 0%, var(--photo-dark) 30%, #8d8d8d 50%, var(--photo-light) 75%, #f1f1f1 100%);
  }
  .cover-band {
    position: absolute; left: 0; top: 105px; width: 100%; height: 139px;
    background: var(--indigo); color: #fff;
  }
  .cover-the { position: absolute; left: 70px; top: 12px; font-family: "Playfair Display SC", serif; font-size: 15px; letter-spacing: 1px; line-height: 1; }
  .cover-script { position: absolute; left: 90px; top: 14px; font-family: "Allura", cursive; font-size: 64px; line-height: 1; white-space: nowrap; }
  .cover-sub { position: absolute; left: 88px; top: 80px; font-family: "Playfair Display SC", serif; font-size: 19px; letter-spacing: 0.5px; line-height: 1; white-space: nowrap; }
  .cover-aud { position: absolute; left: 0; width: 100%; top: 106px; font-size: 9px; text-align: center; }
  .cover-tag { position: absolute; left: 0; width: 100%; top: 121px; font-size: 6.5px; font-style: italic; text-align: center; }
  .brand-mark { position: absolute; right: 14px; bottom: 9px; display: flex; align-items: center; gap: 3px; }
  .brand-dot { width: 9px; height: 9px; border-radius: 50%; background: var(--indigo); }
  .brand-name { font-size: 9px; font-weight: 600; color: var(--indigo); }
  .brand-tag { position: absolute; right: 14px; bottom: 3px; font-size: 3.5px; color: var(--indigo); }

  /* Text pages */
  .text-page { padding: 22px 46px 0 33px; }
  .intro { font-style: italic; font-size: 6.5px; margin-bottom: 13px; }
  .heading { font-family: "Playfair Display SC", serif; font-size: 30px; font-weight: 400; line-height: 1; margin-bottom: 6px; padding-left: 4px; }
  .body p { font-size: 5.2px; line-height: 1.2; margin-bottom: 4.5px; }
  .body p.lead { font-size: 6.5px; margin-top: 2px; }
  .folio { position: absolute; left: 0; width: 100%; bottom: 18px; text-align: center; font-size: 3.6px; letter-spacing: 0.3px; }
  .col-right .folio { padding-right: 15px; }
  .top-pad { padding-top: 27px; }
  .subhead { font-size: 7.5px; font-weight: 600; }
  .label { font-size: 7px; font-weight: 500; line-height: 1; }
  .quote { text-align: center; font-style: italic; font-size: 5.4px; margin: 7px 0 1px; }
  .quote-by { text-align: center; font-size: 5px; margin-bottom: 12px; }
  .pillars { text-align: center; font-family: "Playfair Display SC", serif; font-size: 8px; letter-spacing: 0.5px; line-height: 2.5; margin-top: 4px; }

  /* Section dividers */
  .section { background: var(--indigo); color: #fff; text-align: center; border: 1px solid var(--indigo); }
  .section-num { font-family: "EB Garamond", serif; font-size: 76px; line-height: 1; margin-top: 68px; }
  .section-title { font-family: "EB Garamond", serif; font-size: 33px; line-height: 1.2; letter-spacing: 0.5px; margin-top: 8px; }
  .section.two .section-num { margin-top: 44px; }
</style>
</head>
<body>

<section class="page cover col-left row-1">
  <div class="cover-photo" role="img" aria-label="Black and white portrait of the coach seated outdoors beside a stone wall"></div>
  <div class="cover-band">
    <span class="cover-the">THE</span>
    <span class="cover-script">Personal</span>
    <div class="cover-sub">BRAND FORMULA</div>
    <div class="cover-aud">For Pharmacy Entrepreneurs</div>
    <div class="cover-tag">The quick n' dirty guide to creating a unique personal brand that attracts your ideal clients.</div>
  </div>
  <div class="brand-mark"><span class="brand-dot"></span><span class="brand-name">Corvelta Studio</span></div>
  <div class="brand-tag">Growth with Neighbors</div>
</section>

<section class="page text-page col-right row-1">
  <p class="intro">I'm so glad you're here! Before we start, a few things:</p>
  <h2 class="heading">What this is:</h2>
  <div class="body">
    <p>The Personal Brand Formula consists of the exact steps I take to create unique and authentic brands for my clients. It is also what will drive your entire marketing strategy.</p>
    <p>One mistake I see entrepreneurs make is to consider BRAND as a separate entity from MARKETING. These two essential elements of your business are deeply connected.</p>
    <p>Rather than giving you the elements of a brand, which is really the end product of this work – what I'm giving you here are the essential building blocks, designed to help you discover and unleash your unique brand.</p>
    <p>This is what most people don't tell you about because it's the deep work that happens in the background.</p>
    <p>When you go through the steps to create your own brand, not only do you build a brand that attracts your ideal clients, but your marketing falls into place, and you finally learn what makes you stand way above the competition.</p>
    <p>Yes, it's true. When you take the time to create your brand, your messaging and marketing strategy fall into place. And this formula is what gets you there.</p>
  </div>
  <div class="folio">PAGE X OF XX</div>
</section>

<section class="page text-page col-left row-2">
  <p class="intro">I'm so glad you're here! Before we start, a few things:</p>
  <h2 class="heading">Who this is for:</h2>
  <div class="body">
    <p>The Personal Brand Formula is for you if you're a pharmacy entrepreneur who is starting or already running a business or practice. You may be moving a brick and mortar business online; creating a new business as a coach, patient advocate or navigator; or developing a service that will help your peers or patients.</p>
    <p>If you already have a business, you feel frustrated because you're not attracting your ideal clients – the type of clients you know you're meant to serve. And you don't know how you'll continue to expand your business.</p>
    <p>If you're in start-up, you understand that now is the time to nail down the right brand image and messaging so you can come out of the gate running, rather than wasting your precious time and money on tactics that don't work.</p>
    <p class="lead">Long story short, you're ready to step it up, get noticed, and grow your client base.</p>
  </div>
  <div class="folio">PAGE X OF XX</div>
</section>

<section class="page section col-right row-2">
  <div class="section-num">1</div>
  <div class="section-title">START HERE</div>
</section>

<section class="page text-page top-pad col-left row-3">
  <div class="body">
    <p><span class="subhead">Freedom, impact, and profit…</span><br>one or all of these are the reasons you started, or want to start, a business…</p>
    <p>But right now, you're wondering how you're going to stand out from all the online noise.</p>
    <p>Friendloop is supersaturated with experts and businesses offering very similar if not exactly the same things you do, which makes you doubt how doable and realistic this business thing really is.</p>
    <p>Naturally, when faced with this, you rush to create a logo, a website, and a presence on social media. And this is when I start to worry.</p>
    <p>Because that is COMPLETELY BACKWARDS!</p>
    <p>It's similar to a doctor prescribing medications to treat a patient's symptoms without identifying and understanding what is causing them. The symptoms could be side effects of another medicine, the results of illness, or could stem from any number of issues.</p>
    <p>Writing your website copy without knowing how to stand apart from others in your industry, position yourself as the expert, or the exact words and phrases that will get your ideal client's attention is a big waste of your time and money.</p>
    <p>When I see business owners do this, their eBook doesn't perform as they expected, their website is dead in the water, and they can't seem to get the right clients.</p>
    <p>What I do for my clients, before I can even begin thinking about their marketing, is to DEFINE them… figure out who they are, what they're about, and how to differentiate them so they'll stand out from all the online noise.</p>
    <p>This is the way to build a strong and authentic brand.</p>
  </div>
  <div class="folio">PAGE X OF XX</div>
</section>

<section class="page section two col-right row-3">
  <div class="section-num">2</div>
  <div class="section-title">WHAT IS<br>BRANDING,<br>ANYWAY?</div>
</section>

<section class="page text-page top-pad col-left row-4">
  <div class="body">
    <p><span class="label">BRANDING IS NOT</span><br>Branding is NOT your logo, colors, and fonts. That is visual branding, and you cannot create that until you have defined your brand.</p>
    <p><span class="label">BRANDING IS</span><br>Branding is how you make someone feel after they've heard you talk, read your blog post, visited your website…</p>
    <p>Your brand has an essence, a personality, a definitive way of communicating. Your brand tells your story, speaks to your ideal client in a language they understand and causes them to have an emotional reaction.</p>
  </div>
  <p class="quote">"Your brand is what other people say about you when you're not in the room."</p>
  <p class="quote-by">– <b>Dale Markham</b>, the founder of Northwind Goods</p>
  <div class="body">
    <p>When people know and trust your brand, they become clients. To have a credible and influential personal brand, you need to be able to articulate three things:</p>
  </div>
  <div class="pillars">WHO YOU ARE<br>WHAT YOU DO<br>HOW YOU DO IT</div>
  <div class="folio">PAGE X OF XX</div>
</section>

<section class="page text-page top-pad col-right row-4">
  <div class="body">
    <p>Your personal brand will define how you present yourself on all your marketing platforms – on and off-line. It's everything you and your team say and do. It's what you blog about, how you write, the photos you share. It's the message that comes through loud and clear every time, even when no words are uttered.</p>
    <p>Without a brand, you fade into online oblivion.</p>
    <p>This is your foundation and the BLUEPRINT for all you do.</p>
  </div>
  <div class="folio">PAGE X OF XX</div>
</section>

</body>
</html>
```